iWebSentry flyer internet security for families

We need a flyer design A5 size for distribution by hand and in magazines.

iWebSentry is a service used to protect families online when using all types of devices, on Wi-Fi and mobile network connections.

the website is www.iwebsentry-demo.co.uk

The ad should communicate ease of use, and should be aimed at parents with children between the ages of 3-18. The advert should be communicative but not have lots of text or words.

attached logo designs.

Reason: Extended deadline as have not had time to review the designs due to preparing for service launch on Monday

Industry/Entity Type

Internet

Requirements
Must have
• The 30 day free trial
• Icons for the different platforms that it works on
• emphasis on the features of the product without too much text
• web address www.iwebsentry-demo.co.uk
• info@iwebsentry-demo.co.uk
Nice to have
• A picture of a family including grandparents, parents and children all using devices.
Should not have
• Any of the pricing
• Too much text

```html
<!DOCTYPE html>
<html lang="en">
<head>
<meta charset="utf-8">
<title>iWebSentry – Protect Your Family Online</title>
<link rel="stylesheet" href="https://fonts.googleapis.com/css2?family=Exo+2:wght@500;600;700&family=Open+Sans:wght@400;600;700&display=swap">
<style>
:root{
  --navy:#0d3a55;
  --navy-deep:#08263a;
  --blue:#1f8fcf;
  --blue-mid:#2ea3df;
  --sky:#8fd6f5;
  --orange:#f07d12;
  --orange-light:#f9a21d;
  --ink:#1d1d1f;
  --paper:#ffffff;
  --mist:#e9ebed;
  --grey-text:#333;
}
*{margin:0;padding:0;box-sizing:border-box}
html,body{width:902px;height:1200px;overflow:hidden;background:#f2f2f2}
.flyer{position:relative;width:902px;height:1200px;overflow:hidden;background:var(--paper);font-family:"Open Sans",Arial,sans-serif}
.flyer-bg{position:absolute;inset:0;width:902px;height:1200px}
.abs{position:absolute}
.brand{left:600px;top:44px;display:flex;align-items:center;gap:10px}
.brand-dot{width:46px;height:46px;border-radius:50%;background:var(--navy)}
.brand-name{font-family:"Exo 2",Arial,sans-serif;font-weight:700;font-size:34px;color:var(--navy);letter-spacing:1px}
.headline{left:560px;top:216px;width:286px;text-align:center;font-family:"Exo 2",Arial,sans-serif;font-weight:700;font-size:42px;line-height:51px;color:var(--ink);text-transform:uppercase}
.headline .accent{color:var(--blue)}
.devices-pill{left:556px;top:402px;width:288px;height:36px;border-radius:18px;background:linear-gradient(var(--blue-mid),#1776b3);color:#fff;font-weight:600;font-size:19px;text-align:center;line-height:36px;box-shadow:0 3px 6px rgba(0,0,0,.25)}
.supported-label{left:556px;top:452px;width:288px;text-align:center;font-size:15px;font-weight:600;color:var(--ink)}
.platforms{left:560px;top:490px;width:290px;display:grid;grid-template-columns:repeat(3,1fr);row-gap:10px;text-align:center}
.platform{display:flex;flex-direction:column;align-items:center;gap:5px;font-family:"Exo 2",Arial,sans-serif;font-weight:600;font-size:15px;color:var(--navy)}
.platform-mark{width:52px;height:52px;border-radius:50%;background:var(--blue)}
.platform-wide{grid-column:1 / 4}
.photo{left:50px;top:60px;width:470px;height:480px}
.features-intro{left:40px;top:697px;width:820px;text-align:center;font-family:"Exo 2",Arial,sans-serif;font-weight:600;font-size:29px;line-height:35px;text-transform:uppercase;letter-spacing:1px;color:var(--navy-deep)}
.features-intro .light{color:#fff}
.feature{top:814px;width:170px;display:flex;flex-direction:column;align-items:center}
.feature-icon{width:138px;height:138px;border-radius:50%;background:var(--navy);display:flex;align-items:center;justify-content:center;box-shadow:0 5px 10px rgba(0,0,0,.3)}
.feature-icon .ring{width:122px;height:122px;border-radius:50%;background:#fff;display:flex;align-items:center;justify-content:center}
.feature-label{margin-top:8px;width:154px;min-height:50px;border-radius:10px;background:linear-gradient(#fff,#dcdcdc);box-shadow:0 3px 6px rgba(0,0,0,.3);display:flex;align-items:center;justify-content:center;text-align:center;font-size:16px;font-weight:600;line-height:19px;color:var(--ink);padding:4px 10px}
.feature-label.large{font-size:19px}
.contact{left:150px;top:1124px;color:#fff;font-size:19px;line-height:29px}
.contact-row{display:flex;align-items:center;gap:12px}
.contact-row svg{flex:none}
.social{left:458px;top:1130px;display:flex;align-items:center;gap:12px;color:#fff}
.social-title{font-size:20px;font-weight:600;margin-right:4px}
.social-item{display:flex;align-items:center;gap:5px;font-size:13px;font-weight:600}
.social-dot{width:26px;height:26px;border-radius:50%;background:var(--orange)}
.badge{left:170px;top:428px;width:236px;height:236px}
</style>
</head>
<body>
<main class="flyer">
  <svg class="flyer-bg" viewBox="0 0 902 1200" aria-hidden="true">
    <defs>
      <linearGradient id="topBand" x1="0" y1="0" x2="1" y2="0">
        <stop offset="0" stop-color="#0a3650"/><stop offset=".55" stop-color="#2b8fc6"/><stop offset="1" stop-color="#0d4a6e"/>
      </linearGradient>
      <linearGradient id="greyWash" x1="0" y1="0" x2="1" y2="0">
        <stop offset="0" stop-color="#ffffff"/><stop offset="1" stop-color="#e4e6e8"/>
      </linearGradient>
      <radialGradient id="featureField" cx=".5" cy=".45" r=".7">
        <stop offset="0" stop-color="#a8e2f8"/><stop offset=".55" stop-color="#3fb0e6"/><stop offset="1" stop-color="#1a8cce"/>
      </radialGradient>
      <linearGradient id="footer" x1="0" y1="0" x2="0" y2="1">
        <stop offset="0" stop-color="#0f4464"/><stop offset="1" stop-color="#06202f"/>
      </linearGradient>
    </defs>
    <rect width="902" height="1200" fill="url(#greyWash)"/>
    <!-- top swoosh -->
    <path d="M0 0H902V150C780 120 650 70 560 10L520 0Z" fill="#fff"/>
    <path d="M0 0H470C560 60 700 125 902 155V160C680 150 420 110 0 60Z" fill="url(#topBand)"/>
    <path d="M400 0H440C520 60 680 130 902 150V162C690 148 500 80 400 0Z" fill="var(--orange)"/>
    <path d="M0 40C150 100 350 140 600 160C720 168 820 165 902 160V172C700 185 400 160 0 75Z" fill="#0d3a55" opacity=".15"/>
    <!-- shield -->
    <path d="M284 38L538 140V330C538 450 430 530 284 568C138 530 30 450 30 330V140Z" fill="var(--blue)"/>
    <path d="M284 52L524 148V330C524 440 424 514 284 552C144 514 44 440 44 330V148Z" fill="#fff"/>
    <!-- lower blue field -->
    <path d="M0 620C200 580 450 600 902 740V1200H0Z" fill="url(#featureField)"/>
    <path d="M0 588C260 560 520 590 902 712V730C520 610 260 590 0 620Z" fill="var(--navy)"/>
    <path d="M0 578C260 548 520 578 902 700V712C520 590 260 560 0 588Z" fill="var(--orange)"/>
    <!-- footer -->
    <path d="M0 1080C300 1060 600 1080 902 1120V1200H0Z" fill="var(--orange)"/>
    <path d="M0 1090C300 1070 600 1090 902 1132V1200H0Z" fill="#fff"/>
    <path d="M0 1100C300 1082 600 1100 902 1142V1200H0Z" fill="url(#footer)"/>
  </svg>

  <div class="abs brand"><span class="brand-dot"></span><span class="brand-name">iWebSentry</span></div>

  <div class="abs photo" role="img" aria-label="Photo of a smiling family – grandparents, parents and two children – gathered around a laptop"
       style="clip-path:polygon(50% 0,100% 18%,100% 57%,50% 100%,0 57%,0 18%);background:linear-gradient(160deg,#efe7dc,#cdb9a3 55%,#9d8571)"></div>

  <svg class="abs badge" viewBox="0 0 236 236" aria-hidden="true">
    <polygon fill="var(--orange-light)" stroke="#fff" stroke-width="4"
      points="118,4 133,34 160,14 166,47 198,38 193,71 226,74 208,102 232,118 208,134 226,162 193,165 198,198 166,189 160,222 133,202 118,232 103,202 76,222 70,189 38,198 43,165 10,162 28,134 4,118 28,102 10,74 43,71 38,38 70,47 76,14 103,34"/>
    <path d="M6 150L224 96L232 140L14 196Z" fill="var(--navy)" stroke="#fff" stroke-width="3"/>
    <text x="118" y="100" text-anchor="middle" transform="rotate(-14 118 100)" font-family="Exo 2, sans-serif" font-weight="700" font-size="34" fill="#111">30 DAYS</text>
    <text x="122" y="160" text-anchor="middle" transform="rotate(-14 122 160)" font-family="Exo 2, sans-serif" font-weight="700" font-size="34" fill="#fff">FREE TRIAL</text>
  </svg>

  <h1 class="abs headline">Protect<br><span class="accent">Your Family</span><br>Online</h1>

  <div class="abs devices-pill">Supports Multiple Devices</div>
  <p class="abs supported-label">Supported on</p>
  <div class="abs platforms">
    <div class="platform"><span class="platform-mark"></span>Panelix</div>
    <div class="platform"><span class="platform-mark"></span>Robodroid</div>
    <div class="platform"><span class="platform-mark"></span>PearOS</div>
    <div class="platform platform-wide" style="font-size:26px;color:var(--orange);font-weight:500">ReadSlate</div>
  </div>

  <h2 class="abs features-intro">iWebSentry will protect a device<br>on a Wi-Fi connection, 3G and 4G and has<br><span class="light">the following features</span></h2>

  <div class="abs feature" style="left:71px">
    <div class="feature-icon"><div class="ring">
      <svg width="76" height="70" viewBox="0 0 76 70" aria-hidden="true">
        <rect x="4" y="8" width="54" height="50" rx="4" fill="none" stroke="var(--orange)" stroke-width="5"/>
        <rect x="4" y="8" width="54" height="12" fill="var(--orange)"/>
        <rect x="14" y="2" width="5" height="12" fill="var(--orange)"/><rect x="43" y="2" width="5" height="12" fill="var(--orange)"/>
        <g fill="var(--orange)"><rect x="12" y="26" width="8" height="7"/><rect x="24" y="26" width="8" height="7"/><rect x="36" y="26" width="8" height="7"/><rect x="12" y="38" width="8" height="7"/><rect x="24" y="38" width="8" height="7"/></g>
        <circle cx="56" cy="50" r="16" fill="#fff" stroke="var(--blue)" stroke-width="5"/>
        <path d="M56 42V51H63" fill="none" stroke="var(--blue)" stroke-width="4"/>
      </svg>
    </div></div>
    <div class="feature-label">Device access times</div>
  </div>

  <div class="abs feature" style="left:360px">
    <div class="feature-icon"><div class="ring">
      <svg width="76" height="70" viewBox="0 0 76 70" aria-hidden="true">
        <rect x="2" y="6" width="58" height="42" rx="3" fill="#fff" stroke="var(--blue)" stroke-width="4"/>
        <rect x="2" y="6" width="58" height="9" fill="var(--blue)"/>
        <text x="8" y="34" font-family="Open Sans, sans-serif" font-weight="700" font-size="13" fill="var(--blue)">www</text>
        <path d="M46 40V32A10 10 0 0 1 66 32V40" fill="none" stroke="var(--orange)" stroke-width="5"/>
        <rect x="40" y="40" width="32" height="26" rx="3" fill="var(--orange)"/>
        <circle cx="56" cy="51" r="4" fill="#fff"/>
      </svg>
    </div></div>
    <div class="feature-label">Anti phishing filter</div>
  </div>

  <div class="abs feature" style="left:648px">
    <div class="feature-icon"><div class="ring">
      <svg width="76" height="70" viewBox="0 0 76 70" aria-hidden="true">
        <rect x="4" y="6" width="68" height="46" rx="3" fill="var(--orange)"/>
        <rect x="10" y="12" width="56" height="34" fill="#fff"/>
        <g fill="var(--blue)"><rect x="16" y="32" width="6" height="10"/><rect x="26" y="26" width="6" height="16"/><rect x="36" y="30" width="6" height="12"/><rect x="46" y="22" width="6" height="20"/><rect x="56" y="18" width="6" height="24"/></g>
        <polyline points="14,28 28,20 40,26 58,14" fill="none" stroke="var(--navy)" stroke-width="2"/>
        <rect x="32" y="52" width="12" height="8" fill="var(--orange)"/><rect x="22" y="60" width="32" height="5" rx="2" fill="var(--orange)"/>
      </svg>
    </div></div>
    <div class="feature-label large">Dashboard</div>
  </div>

  <address class="abs contact" style="font-style:normal">
    <div class="contact-row">
      <svg width="18" height="14" viewBox="0 0 18 14" aria-hidden="true"><rect x="1" y="1" width="16" height="12" fill="none" stroke="var(--orange)" stroke-width="2"/><path d="M1 1L9 8L17 1" fill="none" stroke="var(--orange)" stroke-width="2"/></svg>
      info@iwebsentry-demo.co.uk</div>
    <div class="contact-row">
      <svg width="18" height="18" viewBox="0 0 18 18" aria-hidden="true"><g fill="none" stroke="var(--orange)" stroke-width="1.8"><circle cx="9" cy="9" r="8"/><ellipse cx="9" cy="9" rx="3.5" ry="8"/><path d="M1 9H17"/></g></svg>
      www.iwebsentry-demo.co.uk</div>
  </address>

  <div class="abs social">
    <span class="social-title">Get Connected</span>
    <span class="social-item"><span class="social-dot"></span>FaceSpace</span>
    <span class="social-item"><span class="social-dot"></span>Chirper</span>
  </div>
</main>
</body>
</html>
```